Personal Home Page

I'm an independent film maker that recently graduated with a master's in film making, I have done many short films and won awards, I have worked on many other film projects.
I like to have a single home page that's interactive, think crazy, funny, weired is very much welcome (rex hadley kinda) the sole purpose of this page is to promote myself and what I do very briefly with contact details, in a way if anyone goes to the site gets drown in and has fun viewing or experiencing it ! I love the magic designers bring to the table, I'm very open for any creative inputs, thanks
Here are just some examples of what I mean by interactive or entertaining :
http://www.plumreels.com.sg/
http://www.brisklane.com/
Reason: the designs submitted didn't meet the requirements in the brief
Target Market(s)
movie lovers, younger generation, art lovers, media production proffesionals
Requirements
Must have
- contact details, just an email would be enough !
Nice to have
- things relate to movie making, camera, film rolling...etc. but it's not a must
Should not have
- adult material, frightening elements (sudden loud scream or so)
A template that I can get for free online or build on qorv.com

```html
<!DOCTYPE html>
<html lang="en">
<head>
<meta charset="utf-8">
<title>Rex Hadley Kinda — Independent Film Maker</title>
<link rel="stylesheet" href="https://fonts.googleapis.com/css2?family=Fira+Sans+Condensed:ital,wght@0,400;0,500;1,400&family=Arimo:ital,wght@0,400;0,700;1,400&display=swap">
<style>
:root{
  --bg:#1b1b1b;
  --rule:#333333;
  --text:#9a9a9a;
  --white:#f2f2f2;
  --accent:#2aa9e0;
  --accent-bright:#1fb6ee;
  --field:#141414;
  --gold:#c9a23a;
}
*{margin:0;padding:0;box-sizing:border-box}
html,body{width:760px;height:1200px;overflow:hidden}
body{
  position:relative;
  background:
    radial-gradient(ellipse 340px 180px at 380px 80px,#2c2c2c 0%,rgba(27,27,27,0) 100%),
    repeating-linear-gradient(90deg,#1d1d1d 0 3px,#1a1a1a 3px 6px);
  background-color:var(--bg);
  font-family:"Arimo",Arial,sans-serif;
  color:var(--text);
}
h1,h2,h3{font-weight:400}
.abs{position:absolute}
.heading{position:absolute;font-family:"Fira Sans Condensed",sans-serif;font-style:italic;font-weight:400;font-size:18px;line-height:22px;color:var(--white);letter-spacing:-.2px}
.rule{position:absolute;height:1px;background:var(--rule);box-shadow:0 1px 0 #222}

/* header */
.reel-glow{left:212px;top:0;width:110px;height:110px;border-radius:50%;
  background:radial-gradient(circle,#2e2e2e 0%,#242424 60%,rgba(30,30,30,0) 72%)}
.brand-mark{left:265px;top:55px;width:28px;height:28px;background:var(--accent);border-radius:3px}
.brand-name{left:302px;top:50px;font-family:"Fira Sans Condensed",sans-serif;font-weight:500;font-size:30px;color:var(--white);line-height:36px}
.tagline{left:305px;top:84px;font-size:8px;letter-spacing:2.1px;color:#666}

.nav{left:0;top:149px;width:760px;height:16px}
.nav a{position:absolute;top:0;font-family:"Arimo",sans-serif;font-size:10.5px;color:#e6e6e6;text-decoration:none}
.nav a.is-active::after{content:"";position:absolute;left:-2px;right:-2px;top:14px;height:3px;background:var(--accent);border-radius:1px}
.nav-line{left:230px;top:172px;width:300px;height:1px;background:linear-gradient(90deg,rgba(42,169,224,0),rgba(42,169,224,.6),rgba(42,169,224,0))}

/* showcase */
.clapper{left:80px;top:196px;width:174px;height:230px;
  background:linear-gradient(180deg,#4a4a4a 0%,#2a2a2a 45%,#1e1e1e 75%,rgba(27,27,27,0) 100%);border-radius:4px}
.video{left:271px;top:196px;width:406px;height:246px;background:#000}
.video-frame{left:0;top:0;width:406px;height:228px;background:radial-gradient(ellipse 120px 110px at 200px 110px,#3a3a3a 0%,#141414 70%,#050505 100%)}
.video-bar{left:0;top:228px;width:406px;height:18px;background:linear-gradient(#2a2a2a,#1a1a1a);border-top:2px solid #b31b1b}
.video-time{left:61px;top:5px;font-size:7px;color:#cfcfcf}

/* recent work */
.reel-icon{left:80px;top:484px;width:92px;height:32px;border-radius:16px;background:linear-gradient(90deg,#2b2b2b,#6a6a6a,#3a3a3a)}
.work-thumb{position:absolute;left:75px;width:132px;height:82px;border:1px solid var(--accent)}
.work-title{position:absolute;left:217px;font-family:"Fira Sans Condensed",sans-serif;font-weight:400;font-size:14px;line-height:18px;color:var(--accent)}
.work-text{position:absolute;left:217px;width:254px;font-size:7.6px;line-height:12.5px;color:var(--text)}

/* sidebar */
.quote{left:494px;top:529px;width:186px;font-size:7.6px;line-height:12.6px;font-style:italic;color:var(--text)}
.quote b{font-style:normal;color:var(--accent-bright);font-weight:700;margin-left:4px}
.award-icon{left:494px;top:677px;width:28px;height:30px;border-radius:50%;background:radial-gradient(circle at 40% 35%,#e8c560,var(--gold) 60%,#8a6a1c)}
.award-text{left:528px;top:685px;font-family:"Fira Sans Condensed",sans-serif;font-weight:400;font-size:11.5px;color:var(--accent)}
.connect{left:493px;top:755px;width:192px;height:45px;background:var(--accent-bright);border-radius:5px;display:flex;align-items:center;justify-content:space-around;padding:0 8px}
.connect a{font-family:"Arimo",sans-serif;font-size:9px;font-weight:700;color:#0d3c52;text-decoration:none;display:flex;align-items:center;gap:3px}
.connect a::before{content:"";width:6px;height:6px;background:#0d3c52;border-radius:1px}

/* about */
.about-photo{left:76px;top:848px;width:86px;height:85px;border:1px solid var(--accent);border-radius:6px;background:linear-gradient(135deg,#d9d9d9,#6b6b6b 55%,#111)}
.about-title{left:175px;top:845px;font-family:"Fira Sans Condensed",sans-serif;font-weight:400;font-size:14px;line-height:18px;color:var(--accent)}
.about-text{left:175px;top:866px;width:508px;font-size:7.6px;line-height:12.6px;color:var(--text)}

/* contact */
.field{position:absolute;background:var(--field);border:1px solid #222;border-radius:2px;font-size:7.5px;color:#5e5e5e;padding:6px 7px}
.send{left:209px;top:1087px;width:47px;height:18px;border-radius:3px;background:linear-gradient(#3cc3f3,#1593c9);color:#fff;font-family:"Fira Sans Condensed",sans-serif;font-size:9.5px;text-align:center;line-height:18px}
.contact-info{left:494px;font-size:7.6px;line-height:12.6px;color:var(--text)}
.info-icon{left:494px;top:1037px;width:21px;height:21px;border-radius:3px;background:var(--accent)}
.contact-email{left:520px;top:1035px;font-size:7.6px;line-height:12.6px;color:#cfcfcf}
.contact-email a{color:var(--accent);text-decoration:underline}
.copyright{right:92px;top:1161px;font-size:7.6px;color:#a8a8a8}
</style>
</head>
<body>

<header>
  <div class="abs reel-glow" role="img" aria-label="Faint film reel backdrop"></div>
  <div class="abs brand-mark"></div>
  <div class="abs brand-name">Rex Hadley Kinda</div>
  <div class="abs tagline">I'm an independent film maker</div>
  <nav class="abs nav">
    <a class="is-active" href="#" style="left:244px">Home</a>
    <a href="#" style="left:293px">Archive</a>
    <a href="#" style="left:349px">About</a>
    <a href="#" style="left:401px">Resume</a>
    <a href="#" style="left:459px">Blog</a>
    <a href="#" style="left:503px">Contact</a>
  </nav>
  <div class="abs nav-line"></div>
</header>

<section>
  <div class="abs clapper" role="img" aria-label="Illustration of a film clapperboard"></div>
  <div class="abs video">
    <div class="abs video-frame" role="img" aria-label="Still from a short film"></div>
    <div class="abs video-bar">
      <svg class="abs" style="left:12px;top:4px" width="30" height="10" viewBox="0 0 30 10">
        <rect x="1" y="1" width="2" height="8" fill="#cfcfcf"/><rect x="5" y="1" width="2" height="8" fill="#cfcfcf"/>
        <path d="M26 2v6l-3-2h-2V4h2z" fill="#cfcfcf"/>
      </svg>
      <div class="abs video-time">0:00 / 9:38</div>
      <svg class="abs" style="left:292px;top:3px" width="110" height="12" viewBox="0 0 110 12">
        <rect x="2" y="3" width="10" height="6" rx="1" fill="none" stroke="#bbb"/>
        <circle cx="25" cy="6" r="4" fill="#bbb"/>
        <circle cx="45" cy="6" r="4" fill="#bbb"/>
        <rect x="62" y="3" width="10" height="6" fill="none" stroke="#bbb"/>
        <rect x="80" y="2" width="12" height="8" fill="none" stroke="#bbb"/>
        <path d="M97 2h3M97 2v3M108 2h-3M108 2v3M97 10h3M97 10v-3M108 10h-3M108 10v-3" stroke="#bbb"/>
      </svg>
    </div>
  </div>
</section>

<main>
  <div class="abs reel-icon" role="img" aria-label="Film reel icon"></div>
  <h2 class="heading" style="left:180px;top:494px">Recent work</h2>
  <div class="rule" style="left:75px;top:520px;width:400px"></div>

  <div class="work-thumb" style="top:531px;background:linear-gradient(135deg,#2d4a5c,#14242e)" role="img" aria-label="Short film still"></div>
  <h3 class="work-title" style="top:534px">Short films</h3>
  <p class="work-text" style="top:557px">Lorem Ipsum is simply dummy text of the printing and typesetting industry. Lorem Ipsum has been the industry's standard dummy text ever scrambled it to make a type specimen book. It has survived not only five centuries, but also the leap into electronic typesetting.</p>

  <div class="work-thumb" style="top:622px;background:linear-gradient(135deg,#5a5a5a,#151515)" role="img" aria-label="Short film still"></div>
  <h3 class="work-title" style="top:624px">Short films</h3>
  <p class="work-text" style="top:646px">Lorem Ipsum is simply dummy text of the printing and typesetting industry. Lorem Ipsum has been the industry's standard dummy text ever scrambled it to make a type specimen book. It has survived not only five centuries, but also the leap into electronic typesetting.</p>

  <div class="work-thumb" style="top:713px;background:linear-gradient(135deg,#3a4034,#141612)" role="img" aria-label="Short film still"></div>
  <h3 class="work-title" style="top:716px">Short films</h3>
  <p class="work-text" style="top:738px">Lorem Ipsum is simply dummy text of the printing and typesetting industry. Lorem Ipsum has been the industry's standard dummy text ever scrambled it to make a type specimen book. It has survived not only five centuries, but also the leap into electronic typesetting.</p>

  <h2 class="heading" style="left:494px;top:494px">Testimonials</h2>
  <div class="rule" style="left:494px;top:520px;width:190px"></div>
  <p class="abs quote">"Lorem ipsum dolor sit amet, consectetur adipisicing elit, sed do eiusmod tempor incididunt ut labore et dolore magna aliqua. Ut enim ad minim veniam, quis nostrud exercitation ullamco laboris nisi ut aliquip ex ea commodo consequat. Duis aute irure dolor in reprehenderit in voluptate velit esse cillum dolore eu fugiat nulla pariatur"<b>Mara Quill</b></p>

  <h2 class="heading" style="left:494px;top:645px">Awards</h2>
  <div class="rule" style="left:494px;top:670px;width:190px"></div>
  <div class="abs award-icon"></div>
  <div class="abs award-text">Lantern Prize for Best Short Film</div>

  <h2 class="heading" style="left:494px;top:719px">Connect</h2>
  <div class="abs connect">
    <a href="#">Wire</a><a href="#">Chirp</a><a href="#">Folio</a><a href="#">Ringo</a><a href="#">Reel</a>
  </div>

  <h2 class="heading" style="left:76px;top:809px">About&nbsp; me</h2>
  <div class="rule" style="left:75px;top:833px;width:608px"></div>
  <div class="abs about-photo" role="img" aria-label="Photo of the film maker behind a camera"></div>
  <h3 class="abs about-title">lorem ipsum dolor sit ametnulla</h3>
  <p class="abs about-text">Lorem ipsum dolor sit amet, consectetur adipisicing elit, sed do eiusmod tempor incididunt ut labore et dolore magna aliqua. Ut enim ad minim veniam, quis nostrud exercitation ullamco laboris nisi ut aliquip ex ea commodo consequat. Ut enim ad minim veniam, quis nostrud exercitation ullamco laboris nisi ut aliquip ex ea commodo consequat. Ut enim ad minim veniam, quis nostrud exercitation ullamco laboris nisi.&nbsp; Lorem ipsum dolor sit amet, consectetur adipisicing elit, sed do eiusmod tempor incididunt ut labore et dolore magna aliqua. Ut enim ad minim veniam, quis nostrud exercitation ullamco laboris nisi ut aliquip ex ea commodo consequat. Ut enim ad minim veniam, quis nostrud exercitation ullamco laboris</p>

  <h2 class="heading" style="left:76px;top:961px">Contact Information</h2>
  <div class="rule" style="left:75px;top:986px;width:608px"></div>
  <div class="field" style="left:76px;top:999px;width:180px;height:22px">Full name</div>
  <div class="field" style="left:76px;top:1028px;width:180px;height:22px">contact@rexhadleykinda.com</div>
  <div class="field" style="left:76px;top:1056px;width:180px;height:22px">Subject</div>
  <div class="abs send">SEND</div>
  <div class="field" style="left:270px;top:999px;width:204px;height:107px">Message goes here</div>

  <p class="abs contact-info" style="top:996px">Lorem ipsum dolor sit<br>amet, consectetur adipisicing elit</p>
  <div class="abs info-icon"></div>
  <p class="abs contact-email"><a href="mailto:contact@rexhadleykinda.com">contact@rexhadleykinda.com</a><br>+00 (0000) 000 xxx</p>
  <p class="abs contact-info" style="top:1067px;width:190px">Lorem ipsum dolor sit amet, consectetur adipisicing elit, sed do eiusmod tempor incididunt ut labore et dolore magna aliqua.</p>
</main>

<footer>
  <div class="rule" style="left:75px;top:1142px;width:608px"></div>
  <p class="abs copyright">© 2012 Rex Hadley. All Rights Reserved.</p>
</footer>

</body>
</html>
```